63Crest Web Design Project

We need a new web site for our company. 63Crest provides a range of location intelligence and marketing services to assist clients in improving their performance. On the location intelligence side we're the local partner for Vorqel Plin (Quill and Lumen) in South Africa, we're the local reseller and can assist company with the implementation and customization - we'll shortly receive the Vorqel partner logo that should also be displayed on the Homepage. On the marketing side, we provide a range of marketing services for example Tenders, Event Management and Copy writing. The company is a blend between a mapping and marketing services company. You can have a look at the existing site at www.63crest.co.za
Updates

Dear designers, the budget for my project has been increased to $700. Looking forward to receiving your designs. Kind regards Tobias

Dear designers - many thanks for all the great designs received to date. We'll provide feedback shortly. Kind regards 63Crest

Target Market(s)

Our target market is public and private organisations, and online customers (those with a web presence) primarily in South Africa

Industry/Entity Type

Marketing

Requirements
Must have
• I have uploaded the latest text and suggested pages at this stage. Important is that it should be easy to edit the pages in an HTML editor, e.g. Frontpage. I suspect that the navigation will be expanded later e.g. careers, success stories - so it should be easy for me add new sections to the navigation later on. I have also uploaded the different 63Crest logo designs. Please include links on the Homepage for Terms and Conditions and PAIA - see www.63crest.co.za - also the Copyright Note at the bottom of every page
Nice to have
• Although we're targeting corporates and government, and online customers, the site should be fresh and easy to navigate. I like the use of photographs on sites and make them look more interesting than simply text. Although we're also providing marketing services, the location intelligence (mapping) and Vorqel Quill/Lumen aspect are perhaps the most important part of the website.

```html
<!DOCTYPE html>
<html lang="en">
<head>
<meta charset="utf-8">
<title>63Crest – Location Intelligence &amp; Marketing</title>
<link rel="stylesheet" href="https://fonts.googleapis.com/css2?family=Open+Sans:wght@300;400;700&family=Rokkitt:wght@400&display=swap">
<style>
:root{
  --red:#e42127;
  --top-dark:#474d57;
  --top-mid:#5a616b;
  --lower:#7b8088;
  --lower-light:#858a91;
  --text-light:#f2f3f5;
  --text-soft:#e3e5e8;
  --nav-text:#dfe2e6;
  --panel:#f4f4f2;
  --panel-text:#5b5f64;
  --white:#ffffff;
}
*{margin:0;padding:0;box-sizing:border-box}
html,body{width:1064px;height:1200px;overflow:hidden}
body{position:relative;background:var(--lower);font-family:"Open Sans",Arial,sans-serif;color:var(--text-light)}
.hero-band{position:absolute;left:0;top:0;width:1064px;height:598px;
  background:linear-gradient(180deg,var(--top-mid) 0%,var(--top-dark) 70%,#3d434c 100%);
  border-bottom:1px solid #8d929a}
.content-band{position:absolute;left:0;top:599px;width:1064px;height:566px;
  background:linear-gradient(180deg,var(--lower-light) 0%,var(--lower) 40%,#70757d 100%)}

.brand{position:absolute;left:443px;top:0;width:179px;height:125px;background:var(--white);
  display:flex;align-items:center;justify-content:center;gap:8px;
  box-shadow:0 6px 10px rgba(0,0,0,.35)}
.brand-dot{width:14px;height:14px;border-radius:50%;background:var(--red)}
.brand-name{font-family:"Open Sans",sans-serif;font-weight:700;font-size:28px;color:var(--red);letter-spacing:-.5px}

.main-nav{position:absolute;top:165px;left:0;width:1064px;height:25px}
.main-nav a{position:absolute;top:0;height:25px;line-height:25px;font-family:"Rokkitt",serif;font-size:14.5px;
  color:var(--nav-text);text-decoration:none;text-transform:uppercase;letter-spacing:.3px}
.main-nav a.active{background:var(--red);color:var(--white);padding:0 10px}

.slider{position:absolute;left:140px;top:226px;width:785px;height:254px;border:3px solid var(--white);
  background:linear-gradient(135deg,#f1e6d2 0%,#f4d9b8 35%,#e9eef2 60%,#f3dcc0 100%);
  box-shadow:0 8px 10px rgba(0,0,0,.3)}
.slider-dots{position:absolute;left:361px;top:228px;display:flex;gap:6px}
.slider-dots span{width:11px;height:11px;border-radius:50%;background:var(--white);box-shadow:0 1px 2px rgba(0,0,0,.4)}
.slider-dots span.on{background:var(--red);border:2px solid var(--white)}
.slider-badge{position:absolute;left:813px;top:428px;width:114px;height:87px;border-radius:10px;
  background:radial-gradient(circle at 65% 60%,#cfd3d6 0%,#8a98a8 35%,#2f7fd0 60%,rgba(47,127,208,0) 75%)}

.tagline{position:absolute;left:140px;top:502px;width:700px;font-weight:300;font-size:18.5px;line-height:28px;color:var(--text-light)}
.tagline strong{font-weight:700}

.link-col{position:absolute;top:621px}
.link-col h2{font-family:"Rokkitt",serif;font-weight:400;font-size:24px;color:var(--white);letter-spacing:.3px}
.link-col h2::after{content:"";display:block;width:80px;height:1px;margin-top:4px;
  background:linear-gradient(90deg,rgba(255,255,255,.5),rgba(255,255,255,0))}
.link-col ul{list-style:none;margin-top:15px}
.link-col li{font-size:12.5px;line-height:14px;color:var(--text-soft);margin-bottom:14px}
.col-about{left:176px}
.col-services{left:434px;width:200px}
.col-products{left:717px}

.divider{position:absolute;left:240px;top:874px;width:600px;height:1px;
  background:linear-gradient(90deg,rgba(255,255,255,0),rgba(255,255,255,.35),rgba(255,255,255,0))}

.map-widget{position:absolute;left:158px;top:903px;width:465px;height:204px;background:var(--panel);
  border:2px solid #fff;box-shadow:0 6px 10px rgba(0,0,0,.3);color:var(--panel-text);
  font-family:Arial,"Open Sans",sans-serif;font-size:10.5px;overflow:hidden}
.map-form{position:absolute;left:10px;top:7px;width:220px}
.map-form h3{font-size:11px;font-weight:400;letter-spacing:.6px;text-transform:uppercase;margin-bottom:11px;line-height:13px}
.map-form label{display:block;font-weight:700;font-size:11px;line-height:14px;color:#3b3e42;letter-spacing:.3px}
.map-form .field{display:inline-block;border:1px solid #9aa0a6;background:#fff;height:15px;line-height:13px;padding:0 3px;color:#222;font-size:10.5px}
.map-form .field.text{width:144px}
.map-form .field.select{width:32px}
.map-form .field.select.wide{width:40px}
.map-form p{line-height:13px;margin-bottom:9px;letter-spacing:.2px}
.map-view{position:absolute;left:230px;top:0;width:233px;height:200px;
  background:linear-gradient(135deg,#d8e2cf 0%,#dfe4d2 45%,#e6e1d2 100%);border-left:1px solid #ccc}

.hero-art{position:absolute;left:661px;top:903px;width:270px;height:236px;
  background:radial-gradient(circle at 42% 45%,#f3f3f3 0%,#e3dcd4 40%,rgba(200,80,80,.35) 55%,rgba(0,0,0,0) 62%),
             radial-gradient(circle at 78% 70%,#3d7fbf 0%,#245d97 18%,rgba(36,93,151,0) 24%)}

.social{position:absolute;left:137px;top:1150px;display:flex;gap:14px}
.social span{display:flex;align-items:center;gap:4px;font-size:10.5px;font-weight:700;color:var(--white)}
.social i{display:block;width:10px;height:10px;border-radius:50%;background:var(--white)}

.site-footer{position:absolute;left:0;top:1165px;width:1064px;height:35px;background:var(--red)}
.site-footer p{position:absolute;left:378px;top:11px;font-size:9px;color:var(--white)}
</style>
</head>
<body>
<div class="hero-band"></div>
<div class="content-band"></div>

<header>
  <div class="brand"><span class="brand-dot"></span><span class="brand-name">63Crest</span></div>
  <nav class="main-nav">
    <a class="active" href="#" style="left:199px">Home</a>
    <a href="#" style="left:331px">About us</a>
    <a href="#" style="left:478px">Services</a>
    <a href="#" style="left:618px">Products</a>
    <a href="#" style="left:768px">Contact us</a>
  </nav>
</header>

<section class="slider" role="img" aria-label="Close-up photograph of a colourful street map with highlighted routes">
  <div class="slider-dots"><span class="on"></span><span></span><span></span><span></span></div>
</section>
<div class="slider-badge" role="img" aria-label="Illustration of a rolled world map with a compass and red pin"></div>

<p class="tagline">63Crest provides a range of <strong>LOCATION INTELLIGENCE</strong> and <strong>MARKETING SERVICE</strong><br>and products to assis clients in improving their performance.</p>

<section class="link-col col-about">
  <h2>About&nbsp; us</h2>
  <ul>
    <li>Introduction</li>
    <li>What makes us different?</li>
    <li>Broad-Based Black</li>
    <li>Economic Empowerment</li>
    <li>Why 63Crest?</li>
  </ul>
</section>
<section class="link-col col-services">
  <h2>Services</h2>
  <ul>
    <li>Marketing Services</li>
    <li>Tender Services, Event Planning and Management, Copywriting</li>
    <li>Consulting</li>
    <li>Project and Programme, Manage-ment, Geographical Information System (GIS), Strategic Marketing</li>
    <li>Software Development</li>
  </ul>
</section>
<section class="link-col col-products">
  <h2>Products</h2>
  <ul>
    <li>Software</li>
    <li>Vorqel Quill API for Business</li>
    <li>Vorqel Lumen Enterprise</li>
    <li>Vorqel Lumen Builder</li>
    <li>Spatial Data</li>
  </ul>
</section>

<div class="divider"></div>

<section class="map-widget">
  <div class="map-form">
    <h3>Customize</h3>
    <label>Address To Map:</label>
    <span class="field text">Harbor Vale</span>
    <p>Example: "Harbor Vale" or "7 Linden Rd, Westmere, NV"</p>
    <label>Zoom Level</label>
    <span class="field select">0 ▾</span>
    <p>-5 = Zoom Out , 5= Zoom In</p>
    <label>Show Pin</label>
    <span class="field select wide">No ▾</span>
    <p>Show or hide the location marker</p>
  </div>
  <div class="map-view" role="img" aria-label="Embedded road map of western North America with zoom controls"></div>
</section>

<div class="hero-art" role="img" aria-label="Illustration of a red pushpin, a map disc and a glossy globe"></div>

<div class="social">
  <span><i></i>Vorqel</span>
  <span><i></i>Yodela</span>
  <span><i></i>Friendra</span>
  <span><i></i>Chirpa</span>
</div>

<footer class="site-footer">
  <p>Terms and Conditions / Copyright 2012 by 63Crest. All Rights Reserved / PAIA</p>
</footer>
</body>
</html>
```